Business card design and logo for plumbing bussiness

We are wanting a logo for a plumbing business is Queensland Australia. KRV Plumbing and Drainage will be doing works on domestic and commercial sites.
Plumbing, drainage and gas works. We are wanting something that will stand out and be noticed. Colours could be black blue and white but open for suggestions.

Target Market(s)

Builders and home renovators

Industry/Entity Type

Plumbing

Contact Information for Business Card

Miles Dorgan - Director
0417 582 913
miles@krvplumbing.example.com.au
QBCC: 847 2106
ABN: 52 319 407 281

Font styles to use
Sans Serif

Colors
000000

Requirements
Must have
• Clear defined branding

```html
<!DOCTYPE html>
<html lang="en">
<head>
<meta charset="utf-8">
<title>KRV Plumbing – Business Card</title>
<link rel="stylesheet" href="https://fonts.googleapis.com/css2?family=Open+Sans:wght@400;600;700&display=swap">
<style>
  :root {
    --bg: #3b3431;
    --card: #121212;
    --card-edge: #1c1c1c;
    --brand-text: #e4e4e4;
    --accent: #1aa3e0;
    --body-text: #f2f2f2;
  }
  * { box-sizing: border-box; margin: 0; padding: 0; }
  html, body {
    width: 1200px;
    height: 844px;
    overflow: hidden;
    background: var(--bg);
    font-family: "Open Sans", Arial, sans-serif;
  }
  .canvas {
    position: relative;
    width: 1200px;
    height: 844px;
  }
  .card {
    position: absolute;
    top: 263px;
    width: 520px;
    height: 318px;
    background: var(--card);
    border: 1px solid var(--card-edge);
    box-shadow: 0 10px 30px rgba(0,0,0,.45);
  }
  .card--front { left: 50px; }
  .card--back { left: 630px; }

  .brand {
    display: flex;
    align-items: center;
    gap: 10px;
    color: var(--brand-text);
    font-weight: 700;
    line-height: 1;
    white-space: nowrap;
  }
  .brand__dot {
    border-radius: 50%;
    background: var(--accent);
    flex: none;
  }
  .card--front .brand {
    position: absolute;
    top: 40px;
    right: 34px;
    font-size: 30px;
    letter-spacing: 1px;
  }
  .card--front .brand__dot { width: 16px; height: 16px; }
  .card--back .brand {
    position: absolute;
    inset: 0;
    justify-content: center;
    font-size: 40px;
    letter-spacing: 2px;
  }
  .card--back .brand__dot { width: 22px; height: 22px; }

  .contact {
    position: absolute;
    right: 34px;
    top: 138px;
    list-style: none;
    text-align: right;
    color: var(--body-text);
    font-size: 13px;
  }
  .contact__item {
    display: flex;
    justify-content: flex-end;
    align-items: center;
    gap: 8px;
    margin-bottom: 12px;
  }
  .contact__icon { width: 12px; height: 12px; fill: var(--accent); flex: none; }

  .person {
    position: absolute;
    left: 34px;
    bottom: 40px;
    color: var(--body-text);
    font-size: 13px;
  }
  .person__name {
    color: var(--accent);
    font-size: 19px;
    font-weight: 700;
    line-height: 1.1;
  }
  .person__role { margin: 4px 0 22px 0; }
  .person__reg { line-height: 1.6; }
  .person__label { color: var(--accent); font-weight: 700; }
</style>
</head>
<body>
<main class="canvas">
  <section class="card card--front" aria-label="Business card front">
    <div class="brand">
      <span class="brand__dot"></span>
      <span class="brand__name">KRV PLUMBING</span>
    </div>

    <ul class="contact">
      <li class="contact__item">
        <span>0417 582 913</span>
        <svg class="contact__icon" viewBox="0 0 24 24" aria-hidden="true">
          <path d="M6.6 10.8a15.1 15.1 0 0 0 6.6 6.6l2.2-2.2a1 1 0 0 1 1-.25 11.4 11.4 0 0 0 3.6.57 1 1 0 0 1 1 1V20a1 1 0 0 1-1 1A17 17 0 0 1 3 4a1 1 0 0 1 1-1h3.5a1 1 0 0 1 1 1c0 1.25.2 2.45.57 3.6a1 1 0 0 1-.25 1z"/>
        </svg>
      </li>
      <li class="contact__item">
        <span>miles@krvplumbing.example.com.au</span>
        <svg class="contact__icon" viewBox="0 0 24 24" aria-hidden="true">
          <path d="M2 5h20v14H2z M3.5 6.5l8.5 6.5 8.5-6.5" fill="var(--accent)" stroke="var(--card)" stroke-width="1.4"/>
        </svg>
      </li>
    </ul>

    <div class="person">
      <p class="person__name">Miles Dorgan</p>
      <p class="person__role">Director</p>
      <p class="person__reg"><span class="person__label">QBCC:</span> 847 2106</p>
      <p class="person__reg"><span class="person__label">ABN:</span> 52 319 407 281</p>
    </div>
  </section>

  <section class="card card--back" aria-label="Business card back">
    <div class="brand">
      <span class="brand__dot"></span>
      <span class="brand__name">KRV PLUMBING</span>
    </div>
  </section>
</main>
</body>
</html>
```